Glow Up by Lakeside 21 day Challenge

We are having a Glow Up by Lakeside Challenge at our fitness studio. We need a poster design using the template attached as a reference. I have also included our Bromalux logo to put on the poster. Please DO NOT use the graphics in the flyer as we are expecting something much better :-)

-Size needed 11x17 with bleeding for printing

-We need this made in Photoshop (CS3 friendly) or at least delivered in PS as we might change some text or re-arrange the design later on.

-We need this in layers.

```html
<!DOCTYPE html>
<html lang="en">
<head>
<meta charset="utf-8">
<title>Glow Up by Lakeside 21 day Challenge</title>
<link rel="stylesheet" href="https://fonts.googleapis.com/css2?family=Anton&family=Arimo:ital@0;1&display=swap">
<style>
  :root {
    --concrete-dark: #c9c9c9;
    --concrete-light: #e6e6e6;
    --paper: #ececec;
    --ink: #111111;
    --red: #d4121a;
    --band-red: #b5141b;
    --white: #ffffff;
    --brand-blue: #3f72b3;
    --skin-deep: #7a4323;
    --skin-mid: #b5773f;
    --sky-glow: #f4f6f3;
    --sky-blue: #b9d3e6;
  }
  * { margin: 0; padding: 0; box-sizing: border-box; }
  html, body { width: 800px; height: 1200px; overflow: hidden; }
  body { font-family: "Arimo", Arial, sans-serif; background: var(--paper); }

  .poster {
    position: relative; width: 800px; height: 1200px; overflow: hidden;
    background: linear-gradient(180deg, var(--concrete-dark) 0%, var(--concrete-light) 30%, var(--paper) 60%, var(--paper) 100%);
  }

  .brand {
    position: absolute; left: 20px; top: 58px;
    display: flex; align-items: center; gap: 8px;
  }
  .brand-mark { width: 18px; height: 18px; background: var(--brand-blue); }
  .brand-name {
    font-family: "Anton", Impact, sans-serif; font-size: 34px; line-height: 1;
    color: var(--brand-blue); letter-spacing: 1px;
  }

  .headline {
    position: absolute; left: 357px; top: 22px; z-index: 2;
    font-family: "Anton", Impact, sans-serif; font-size: 64px; line-height: 1.02;
    text-transform: uppercase; letter-spacing: 2px; color: var(--ink);
  }
  .headline .accent { color: var(--red); }
  .headline .wide { letter-spacing: 3px; }

  .hero-photo {
    position: absolute; left: 0; top: 228px; width: 800px; height: 587px;
    background:
      radial-gradient(circle at 300px 70px, var(--sky-glow) 0 50px, transparent 150px),
      linear-gradient(90deg, var(--skin-deep) 0%, var(--skin-mid) 28%, var(--skin-deep) 52%, var(--sky-blue) 58%, var(--sky-glow) 85%, var(--sky-blue) 100%);
    clip-path: polygon(0 10%, 6% 8%, 14% 9%, 30% 3%, 45% 2%, 60% 1%, 75% 0, 88% 1%, 100% 2%,
      100% 58%, 90% 59%, 80% 64%, 70% 68%, 58% 71%, 48% 77%, 40% 83%, 33% 92%, 30% 100%,
      0 100%);
  }

  .intro {
    position: absolute; left: 437px; top: 330px;
    font-family: "Anton", Impact, sans-serif; font-size: 45px; line-height: 1.0;
    text-transform: uppercase; color: var(--ink); letter-spacing: 0.5px;
  }
  .promise {
    position: absolute; left: 175px; top: 428px;
    font-family: "Anton", Impact, sans-serif; font-size: 67px; line-height: 1.0;
    text-transform: uppercase; letter-spacing: 0.5px;
  }
  .promise .on-photo { color: var(--white); }
  .promise .on-sky { color: var(--ink); }

  .benefits {
    position: absolute; left: 245px; top: 746px; width: 530px; list-style: none;
    font-size: 16.5px; line-height: 1.25; color: var(--ink);
  }
  .benefits li { position: relative; padding-left: 42px; margin-bottom: 18px; }
  .benefits li svg { position: absolute; left: 0; top: 2px; }
  .benefits .num { color: var(--red); font-weight: 700; font-size: 19px; }

  .offer-band {
    position: absolute; left: 0; top: 955px; width: 800px; height: 92px;
    background: var(--band-red);
    clip-path: polygon(0 6%, 10% 0, 25% 5%, 40% 1%, 55% 6%, 70% 0, 85% 5%, 100% 2%,
      100% 94%, 88% 100%, 72% 95%, 58% 100%, 42% 94%, 28% 100%, 12% 95%, 0 100%);
    display: flex; align-items: center; justify-content: center;
  }
  .offer-text {
    font-family: "Anton", Impact, sans-serif; font-size: 37px; color: var(--white);
    letter-spacing: 0.3px;
  }

  .testimonial { position: absolute; left: 88px; top: 1058px; color: var(--red); font-style: italic; }
  .testimonial-label { font-size: 15px; display: block; margin-left: 6px; }
  .testimonial-quote { font-size: 19px; font-style: normal; }
  .testimonial-quote q { quotes: none; }
  .testimonial-author { font-style: italic; margin-left: 26px; }

  .call-to-action {
    position: absolute; left: 0; top: 1122px; width: 800px; text-align: center;
    font-family: "Anton", Impact, sans-serif; font-size: 28px; line-height: 1.2;
    text-transform: uppercase; color: var(--ink); letter-spacing: 0.8px;
  }
</style>
</head>
<body>
<main class="poster">
  <div class="brand">
    <span class="brand-mark"></span>
    <span class="brand-name">BROMALUX</span>
  </div>

  <div class="hero-photo" role="img" aria-label="Photo of a muscular shirtless athlete's torso in front of a sunny beach and sea"></div>

  <h1 class="headline">
    <span class="accent">Glow</span> Up<br>
    By<br>
    <span class="accent wide">Lakeside</span>
  </h1>

  <p class="intro">Discover the<br>secret to a</p>
  <p class="promise">
    <span class="on-photo">Beach Re</span><span class="on-sky">ady Body</span><br>
    <span class="on-photo">In 21 </span><span class="on-sky">Days</span>
  </p>

  <ul class="benefits">
    <li><svg width="22" height="20" viewBox="0 0 22 20"><path d="M2 10 L8 16 L19 2" fill="none" stroke="#d4121a" stroke-width="3.5" stroke-linecap="round"/></svg><span class="num">9</span> total training sessions designed to incinerate fat off your midsection, thighs, and arms</li>
    <li><svg width="22" height="20" viewBox="0 0 22 20"><path d="M2 10 L8 16 L19 2" fill="none" stroke="#d4121a" stroke-width="3.5" stroke-linecap="round"/></svg><span class="num">21</span> days of nutritional guidance, including delicious recipes</li>
    <li><svg width="22" height="20" viewBox="0 0 22 20"><path d="M2 10 L8 16 L19 2" fill="none" stroke="#d4121a" stroke-width="3.5" stroke-linecap="round"/></svg>A Success Session to map out your individual plan for success</li>
    <li><svg width="22" height="20" viewBox="0 0 22 20"><path d="M2 10 L8 16 L19 2" fill="none" stroke="#d4121a" stroke-width="3.5" stroke-linecap="round"/></svg>Your very own Personal Accountability Coach to ensure you get results</li>
  </ul>

  <div class="offer-band">
    <p class="offer-text">You get all this—a $399 value—for ONLY $99!</p>
  </div>

  <blockquote class="testimonial">
    <span class="testimonial-label">Testimonial</span>
    <span class="testimonial-quote"><q>I’ve never been more fit in my life—at age 41!</q><span class="testimonial-author">~Marisol Trevane</span></span>
  </blockquote>

  <p class="call-to-action">Hurry! Space is limited to only 20 participants!!!<br>Claim your spot now: website and phone number</p>
</main>
</body>
</html>
```